Sales and Lettings Boards

Hello, please see attached our sales and lettings boards for our estate agency. These were "designed" by the sign writers. As you can see they are pretty flat and boring - could you work your magic and make them stand out please? I've also attached the logo files. Many thanks, Glen

Target Market(s)

Consumers - residential sale property sales and lettings

Industry/Entity Type

Real Estate Agent

```html
<!DOCTYPE html>
<html lang="en">
<head>
<meta charset="utf-8">
<title>Calder Sales &amp; Lettings – Rooms To Let Board</title>
<link rel="stylesheet" href="https://fonts.googleapis.com/css2?family=Montserrat:wght@700;800&family=Raleway:wght@400;500;900&display=swap">
<style>
  :root {
    --backdrop: #2a2a2a;
    --board-white: #ffffff;
    --charcoal: #454545;
    --brand-green: #62b22f;
    --shadow-tint: rgba(70, 50, 110, 0.35);
  }
  * { margin: 0; padding: 0; box-sizing: border-box; }
  html, body {
    width: 1200px;
    height: 1200px;
    overflow: hidden;
    background: var(--backdrop);
  }
  .canvas {
    position: relative;
    width: 1200px;
    height: 1200px;
  }
  .board {
    position: absolute;
    left: 74px;
    top: 179px;
    width: 1052px;
    height: 841px;
    background: var(--board-white);
  }
  .frame-line {
    position: absolute;
    left: 40px;
    top: 127px;
    width: 972px;
    height: 417px;
  }
  .frame-shadow {
    position: absolute;
    left: 80px;
    top: 540px;
    width: 892px;
    height: 40px;
    border-radius: 50%;
    background: radial-gradient(ellipse at 50% 0%, var(--shadow-tint) 0%, rgba(70,50,110,0.12) 45%, rgba(255,255,255,0) 75%);
  }
  .brand-name {
    position: absolute;
    left: 0;
    top: 48px;
    width: 100%;
    text-align: center;
    font-family: "Montserrat", sans-serif;
    font-weight: 700;
    font-size: 168px;
    line-height: 1;
    letter-spacing: -3px;
    color: var(--charcoal);
  }
  .tagline-band {
    position: absolute;
    left: 169px;
    top: 211px;
    width: 714px;
    height: 66px;
    background: var(--brand-green);
    display: flex;
    align-items: center;
    justify-content: center;
  }
  .tagline {
    font-family: "Raleway", sans-serif;
    font-weight: 500;
    font-size: 50px;
    letter-spacing: 5px;
    color: var(--board-white);
    line-height: 1;
  }
  .headline {
    position: absolute;
    left: 0;
    top: 350px;
    width: 100%;
    text-align: center;
    font-family: "Montserrat", sans-serif;
    font-weight: 800;
    font-size: 122px;
    letter-spacing: -3px;
    line-height: 1;
    color: var(--charcoal);
  }
  .headline .accent { color: var(--brand-green); }
  .contact-strip {
    position: absolute;
    left: 0;
    top: 604px;
    width: 1052px;
    height: 237px;
    background: var(--charcoal);
  }
  .contact-notch {
    position: absolute;
    left: 478px;
    top: 0;
    width: 96px;
    height: 28px;
  }
  .phone {
    position: absolute;
    left: 0;
    top: 36px;
    width: 100%;
    text-align: center;
    font-family: "Raleway", sans-serif;
    font-weight: 900;
    font-size: 118px;
    line-height: 1.1;
    color: var(--brand-green);
    letter-spacing: 1px;
  }
  .website {
    position: absolute;
    left: 0;
    top: 158px;
    width: 100%;
    text-align: center;
    font-family: "Raleway", sans-serif;
    font-weight: 400;
    font-size: 60px;
    line-height: 1;
    color: var(--board-white);
  }
</style>
</head>
<body>
<main class="canvas">
  <section class="board">
    <svg class="frame-line" viewBox="0 0 972 417" aria-hidden="true">
      <polyline points="136,1 1,1 1,416 971,416 971,1 836,1" fill="none" stroke="#62b22f" stroke-width="2"/>
    </svg>
    <div class="frame-shadow" aria-hidden="true"></div>

    <h1 class="brand-name">CALDER</h1>
    <div class="tagline-band"><span class="tagline">SALES &amp; LETTINGS</span></div>

    <h2 class="headline">ROOMS <span class="accent">TO LET</span></h2>

    <footer class="contact-strip">
      <svg class="contact-notch" viewBox="0 0 96 28" aria-hidden="true">
        <polygon points="0,0 96,0 48,28" fill="#ffffff"/>
      </svg>
      <p class="phone">01632 960482</p>
      <p class="website">www.calder-estates.co.uk</p>
    </footer>
  </section>
</main>
</body>
</html>
```